Save The Date Postcard (front and back)

Need a two-sided, save-the-date postcard. The "front" of the card can be any design, but the "back" needs to meet the Varnel Parcel Bureau's mailing requirements (http://brellopress.example/index.iml?mdl=subpage/view.mdl&PAGE_ID=29760).

It's our 90th year holding our "Quorvan Forum," a one-day symposium for cardiologists (heart doctors) to participate in professional development and gain credits for medical education (http://tq-zmb.example/annualmtg18).

Because it's our 90th Anniversary, I was thinking that maybe there could be a cake or cupcake on it. I am also open to other "celebratory" graphic design ideas, as long as they're not too 'childish' looking. This is a *professional* educational event for doctors, *NOT* a party or reception. Design can be a photo or illustration as long as it's tasteful.

Specs:

- Must be rectangular and between 3 1/2 and 4 1/4 inches high and between 5 and 6 inches long. Horizontal (landscape) layout preferred but not required.

- Should feature our logos somewhere: 1) QXBranchMark_EPS-Files.zip, 2) QXHSMark_Blue, 3) HalvernPulseInstituteMarks and 4) 90TH-ANNUAL-QUORVAN-FORUM-MARK / QXHS 90th ANNUAL QUORVAN FORUM mark-cropped

Mandatory copy (in no particular order):

- "Save the Date"
- "Oct. 20" or "Oct. 20th" or "October 20" (whichever looks best)
- The words "New York City" or "NYC"

Optional copy - we prefer a nicer design over tons of copy, but if there's space and the design looks nice, you can add:

- "Celebrating our 90th Annual Quorvan Forum"
- "The Tolliver Hall of the Marbeck Institute of Learning" (the location)
- "Let's cheer to 90 years!"

Target Market(s)

Physicians and nurses (please do not use stock images of doctors or nurses)

Industry/Entity Type

Medical And Science

Colors
0455a3

Requirements
Must have
• - The words "Save The Date"
• - The date (Oct. 20th)
• - 3 of our logos (Chapter, Society and "90th" logo)
• - The words "New York City" or "NYC"
• - Space to put a mailing address and a stamp on the postcard. See regulations: http://brellopress.example/index.iml?mdl=subpage/view.mdl&PAGE_ID=29760
• Must be rectangular and between 3 1/2 and 4 1/4 inches high and between 5 and 6 inches long. Horizontal (landscape) layout preferred but not required.
• - Designer must deliver the raw files (either .ai, .eps, .idml or .psd)
Nice to have
• - Horizontal (landscape) layout preferred
• - A cake or cupcake (not required)
• - The location of the event: "The Tolliver Hall of the Marbeck Institute of Learning" or "The Tolliver Hall at MIOL"
• - Colors that match our color palette (not required) > Sample: http://tq-zmb.example/getting-involved/
Should not have
• - Should not be to childish or unprofessional (take a look at our website for our style)
• - Should not be to "pink" or look too much like a party invitation

```html
<!DOCTYPE html>
<html lang="en">
<head>
<meta charset="utf-8">
<title>Save the Date Postcard – Front and Back</title>
<link rel="stylesheet" href="https://fonts.googleapis.com/css2?family=Montserrat:wght@600;700&family=PT+Sans+Narrow:wght@400;700&display=swap">
<style>
  :root {
    --backdrop: #e9e6e1;
    --panel-lavender: #bcc0d3;
    --brand-navy: #1e2a6e;
    --brand-blue: #0455a3;
    --accent-purple: #8c1f88;
    --faint-lavender: #aab0cc;
    --card-white: #ffffff;
    --ink: #1a1a1a;
    --stamp-grey: #9a9a9a;
    --photo-teal-light: #9ff0df;
    --photo-teal: #62d6c2;
    --photo-pink: #cf6bd6;
  }
  * { margin: 0; padding: 0; box-sizing: border-box; }
  html, body { width: 1200px; height: 462px; overflow: hidden; }
  body {
    position: relative;
    background: var(--backdrop);
    font-family: "PT Sans Narrow", "Arial Narrow", sans-serif;
  }
  .postcard {
    position: absolute;
    top: 47px;
    width: 516px;
    height: 368px;
    overflow: hidden;
    box-shadow: 0 2px 6px rgba(0,0,0,.18);
  }
  .postcard--front { left: 54px; }
  .postcard--back { left: 620px; background: var(--card-white); }

  /* Front */
  .front-panel {
    position: absolute; left: 0; top: 0;
    width: 258px; height: 100%;
    background: var(--panel-lavender);
    text-align: center;
    font-family: "Montserrat", sans-serif;
  }
  .save-badge {
    position: absolute; left: 38px; top: 23px;
    width: 180px; height: 32px;
    background: var(--accent-purple);
    color: var(--card-white);
    font-size: 17px; font-weight: 700; letter-spacing: 1px;
    line-height: 32px;
  }
  .save-badge em { font-style: italic; font-weight: 600; font-size: 14px; text-transform: lowercase; }
  .event-date {
    position: absolute; left: 0; top: 98px; width: 100%;
    color: var(--brand-navy);
    font-size: 19px; font-weight: 700; letter-spacing: 1px;
  }
  .divider {
    position: absolute; left: 96px; width: 58px; height: 3px;
    background: var(--accent-purple);
  }
  .divider--top { top: 114px; }
  .divider--bottom { top: 126px; display: none; }
  .event-venue {
    position: absolute; left: 0; top: 143px; width: 100%;
    color: var(--accent-purple);
    font-size: 14px; font-weight: 700; letter-spacing: 1px; line-height: 19px;
  }
  .event-venue strong { font-size: 17px; }
  .forum-mark {
    position: absolute; left: 54px; top: 206px; width: 150px;
    color: var(--brand-blue);
    font-size: 11px; font-weight: 700; line-height: 14px;
  }
  .partner-mark {
    position: absolute; top: 268px; width: 80px;
    display: flex; flex-direction: column; align-items: center; gap: 4px;
    color: var(--brand-navy);
    font-size: 8px; font-weight: 700; line-height: 10px;
  }
  .partner-mark--society { left: 44px; }
  .partner-mark--institute { left: 134px; }
  .mark-circle {
    width: 42px; height: 42px; border-radius: 50%;
    border: 2px solid var(--brand-navy);
  }
  .cupcake-photo {
    position: absolute; left: 258px; top: 0;
    width: 258px; height: 100%;
    background:
      radial-gradient(circle at 38% 30%, rgba(255,255,255,.85) 0, rgba(255,255,255,0) 22%),
      radial-gradient(ellipse at 48% 75%, var(--photo-pink) 0, rgba(207,107,214,0) 32%),
      linear-gradient(160deg, var(--photo-teal-light), var(--photo-teal));
  }

  /* Back */
  .back-forum-mark {
    position: absolute; left: 44px; top: 26px; width: 190px;
    text-align: center;
    color: var(--faint-lavender);
    font-family: "Montserrat", sans-serif;
    font-weight: 700;
  }
  .back-forum-mark .mark-line { display: block; font-size: 12px; line-height: 15px; }
  .back-forum-mark .mark-figure { display: block; font-size: 58px; line-height: 70px; }
  .chapter-history {
    position: absolute; left: 23px; top: 145px; width: 206px;
    color: var(--ink);
    font-size: 13px; line-height: 15.4px;
  }
  .return-address {
    position: absolute; left: 236px; top: 28px;
    display: flex; gap: 10px;
  }
  .return-address .mark-circle { width: 50px; height: 50px; border-width: 1.5px; border-color: var(--brand-navy); }
  .return-text { font-size: 12px; line-height: 15px; color: var(--ink); }
  .return-text .org-name { font-weight: 700; display: block; margin-bottom: 6px; width: 140px; }
  .stamp-box {
    position: absolute; left: 442px; top: 31px;
    width: 53px; height: 53px;
    border: 3px solid var(--stamp-grey);
  }
</style>
</head>
<body>

<section class="postcard postcard--front" aria-label="Postcard front">
  <div class="front-panel">
    <div class="save-badge">SAVE <em>the</em> DATE</div>
    <div class="divider divider--top" style="top:85px"></div>
    <p class="event-date">OCTOBER 20TH</p>
    <div class="divider" style="top:129px"></div>
    <p class="event-venue">THE TOLLIVER HALL<br>AT <strong>MIOL</strong></p>
    <p class="forum-mark">QXHS 90th Quorvan Forum</p>
    <div class="partner-mark partner-mark--society">
      <span class="mark-circle"></span>
      <span>Quorvan Heart Society</span>
    </div>
    <div class="partner-mark partner-mark--institute">
      <span class="mark-circle"></span>
      <span>Halvern Pulse Institute</span>
    </div>
  </div>
  <div class="cupcake-photo" role="img" aria-label="Cupcake with pink swirled frosting and a lit sparkler on a mint background"></div>
</section>

<section class="postcard postcard--back" aria-label="Postcard back">
  <div class="back-forum-mark">
    <span class="mark-line">THE QUORVAN HEART SOCIETY</span>
    <span class="mark-figure">90th</span>
    <span class="mark-line">ANNUAL QUORVAN FORUM</span>
  </div>
  <p class="chapter-history">The Halvern State Branch of the Quorvan College of Heart Medicine (HQCHM) was founded in 1990, but our history in New York is much older. In fact the Quorvan College of Heart Medicine (QCHM) was started by a group of physicians from New York. The Branch was formed for the purpose of contributing to the prevention of cardiovascular diseases and ensuring optimal quality of care for individuals with such diseases.</p>
  <div class="return-address">
    <span class="mark-circle"></span>
    <p class="return-text">
      <span class="org-name">The Halvern State Branch of the Quorvan College of Heart Medicine</span>
      418 Corliss Avenue, Suite 1206<br>
      Brellton, NY 10418
    </p>
  </div>
  <div class="stamp-box" aria-label="Stamp area"></div>
</section>

</body>
</html>
```